I needed some business cards done for my band. We are a 9 piece funk/horn band that plays a lot of private parties, wedding receptions and music festivals. We'd like a design with vivid colors that incorporates our logo. You can check out our website at www.brasslanternband.example to see what type of vibe we are going for.

```html
<!DOCTYPE html>
<html lang="en">
<head>
<meta charset="utf-8">
<title>Brass Lantern – Business Cards</title>
<link href="https://fonts.googleapis.com/css2?family=Poppins:wght@400;500;600&display=swap" rel="stylesheet">
<style>
  :root {
    --stage: #2a2a2a;
    --card-dark: #1c1c1c;
    --card-light: #ffffff;
    --lime: #c6dc2e;
    --text-light: #f2f2f2;
    --mark-grey: #4a4a4a;
    --ink: #111111;
  }
  html, body {
    margin: 0;
    padding: 0;
    width: 1200px;
    height: 1015px;
    overflow: hidden;
    background: var(--stage);
    font-family: "Poppins", sans-serif;
  }
  .canvas {
    position: relative;
    width: 1200px;
    height: 1015px;
  }
  .card {
    position: absolute;
    left: 320px;
    width: 560px;
    height: 320px;
    background: var(--card-dark);
    box-shadow: 0 10px 28px rgba(0,0,0,0.55);
    overflow: hidden;
  }
  .card--front { top: 150px; }
  .card--back  { top: 530px; }

  .front-name {
    position: absolute;
    inset: 0;
    display: flex;
    align-items: center;
    justify-content: center;
    font-weight: 600;
    font-size: 46px;
    color: var(--mark-grey);
    letter-spacing: 0.5px;
  }

  .back-art {
    position: absolute;
    inset: 0;
  }
  .identity {
    position: absolute;
    left: 40px;
    top: 110px;
  }
  .identity__name {
    margin: 0;
    font-weight: 600;
    font-size: 19px;
    letter-spacing: 1px;
    color: var(--lime);
    text-transform: uppercase;
    line-height: 1.1;
  }
  .identity__role {
    margin: 2px 0 0;
    font-size: 13px;
    color: var(--text-light);
  }
  .address {
    position: absolute;
    left: 62px;
    top: 188px;
    margin: 0;
    font-style: normal;
    font-size: 12px;
    line-height: 1.4;
    color: var(--text-light);
  }
  .contacts {
    position: absolute;
    left: 40px;
    top: 238px;
    margin: 0;
    padding: 0;
    list-style: none;
    font-size: 12px;
    color: var(--text-light);
  }
  .contacts li {
    display: flex;
    align-items: center;
    gap: 8px;
    height: 20px;
  }
  .contacts svg { width: 14px; height: 14px; flex: none; }

  .brand {
    position: absolute;
    left: 360px;
    top: 40px;
    width: 200px;
    text-align: center;
  }
  .brand__dot {
    display: block;
    width: 120px;
    height: 120px;
    margin: 0 auto 10px;
    border-radius: 50%;
    background: var(--lime);
  }
  .brand__name {
    font-weight: 600;
    font-size: 20px;
    color: var(--ink);
  }
</style>
</head>
<body>
<main class="canvas">

  <section class="card card--front" aria-label="Card front">
    <div class="front-name">Brass Lantern</div>
  </section>

  <section class="card card--back" aria-label="Card back">
    <svg class="back-art" viewBox="0 0 560 320" width="560" height="320" aria-hidden="true">
      <circle cx="470" cy="128" r="228" fill="var(--lime)"/>
      <circle cx="482" cy="118" r="224" fill="var(--card-light)"/>
    </svg>

    <div class="identity">
      <p class="identity__name">Marcus Reed</p>
      <p class="identity__role">Managing Director</p>
    </div>

    <address class="address">17 Harbor Street, Suite 4<br>Riverton, 60214</address>

    <ul class="contacts">
      <li>
        <svg viewBox="0 0 24 24" aria-hidden="true"><path fill="var(--lime)" d="M6.6 10.8a15 15 0 0 0 6.6 6.6l2.2-2.2a1 1 0 0 1 1-.25 11.4 11.4 0 0 0 3.6.57 1 1 0 0 1 1 1V20a1 1 0 0 1-1 1A17 17 0 0 1 3 4a1 1 0 0 1 1-1h3.5a1 1 0 0 1 1 1c0 1.25.2 2.45.57 3.57a1 1 0 0 1-.25 1z"/></svg>
        <span>055-210 384 617</span>
      </li>
      <li>
        <svg viewBox="0 0 24 24" aria-hidden="true"><path fill="var(--lime)" d="M2 5h20v14H2z"/><path fill="none" stroke="var(--card-dark)" stroke-width="1.8" d="M2 5l10 8 10-8"/></svg>
        <span>info@brasslanternband.example</span>
      </li>
      <li>
        <svg viewBox="0 0 24 24" aria-hidden="true"><g fill="none" stroke="var(--lime)" stroke-width="2"><circle cx="12" cy="12" r="9.5"/><ellipse cx="12" cy="12" rx="4" ry="9.5"/><path d="M2.5 12h19M4 7h16M4 17h16"/></g></svg>
        <span>www.brasslanternband.example</span>
      </li>
    </ul>

    <div class="brand">
      <span class="brand__dot"></span>
      <span class="brand__name">Brass Lantern</span>
    </div>
  </section>

</main>
</body>
</html>
```